Vesk Architecture

We are a architectural design and build company working between scales 1/1000 to 1/1 we want people to understand our difference from our design experience and quality.we build hotels restourants and office spaces.Our company name is Vesk architecture to mind sustainability.

We want to write our adress phone and work spesifications on the card and we want our logo as backround.

Ps:you could find the logo adress and phone box numbers from the web:www.veskmimarlik-ornek.com

Target Market(s)

Who looks for experts.

Industry/Entity Type

Architecture

Requirements
Must have
• Design is over everything.
Should not have
• we don want it to be colorfull

```html
<!DOCTYPE html>
<html lang="tr">
<head>
<meta charset="utf-8">
<title>Vesk Mimarlık – Kartvizit</title>
<link rel="stylesheet" href="https://fonts.googleapis.com/css2?family=Josefin+Sans:wght@300&family=Jost:wght@400;600&display=swap">
<style>
  :root {
    --paper: #ffffff;
    --ink: #111111;
    --frame: #1a1a1a;
    --band: #c4c4c4;
    --watermark: #d2d2d2;
  }
  html, body {
    margin: 0;
    padding: 0;
    width: 1200px;
    height: 673px;
    overflow: hidden;
    background: var(--paper);
  }
  .business-card {
    display: block;
    width: 1200px;
    height: 673px;
  }
  .card-frame { fill: var(--paper); stroke: var(--frame); stroke-width: 3; }
  .diagonal-band { fill: var(--band); }
  .brand-watermark {
    fill: var(--watermark);
    font-family: "Josefin Sans", sans-serif;
    font-weight: 300;
    font-size: 430px;
  }
  .brand-name {
    fill: var(--ink);
    font-family: "Josefin Sans", sans-serif;
    font-weight: 300;
  }
  .brand-name--word { font-size: 128px; }
  .brand-name--sub { font-size: 31px; letter-spacing: 2px; }
  .person-name {
    fill: var(--ink);
    font-family: "Jost", sans-serif;
    font-weight: 400;
    font-size: 42px;
  }
  .person-title {
    fill: var(--ink);
    font-family: "Jost", sans-serif;
    font-weight: 600;
    font-size: 23px;
    letter-spacing: 9px;
  }
  .contact-line {
    fill: var(--ink);
    font-family: "Jost", sans-serif;
    font-weight: 400;
    font-size: 24px;
  }
  .contact-label { font-weight: 600; }
</style>
</head>
<body>
<svg class="business-card" viewBox="0 0 1100 640" preserveAspectRatio="none" xmlns="http://www.w3.org/2000/svg">
  <defs>
    <clipPath id="card-area">
      <rect x="25" y="27" width="1065" height="590"/>
    </clipPath>
  </defs>

  <rect class="card-frame" x="25" y="27" width="1065" height="590"/>

  <g clip-path="url(#card-area)">
    <text class="brand-watermark" x="150" y="680" textLength="790" lengthAdjust="spacing">vesk</text>
    <polygon class="diagonal-band" points="25,478 1090,120 1090,232 25,548"/>
  </g>

  <g class="brand-lockup">
    <text class="brand-name brand-name--word" x="145" y="200">vesk</text>
    <text class="brand-name brand-name--sub" x="148" y="268">MİMARLIK</text>
  </g>

  <g class="contact-block" transform="translate(980 255) rotate(-18.6)">
    <text class="person-name" x="-3" y="-59" text-anchor="end">Deniz Arda KAYA</text>
    <text class="person-title" x="-3" y="4" text-anchor="end">Mimar</text>

    <text class="contact-line" x="9" y="82" text-anchor="end">Ihlamur Mah. Yesil Cad. Lale Sok.</text>
    <text class="contact-line" x="4" y="116" text-anchor="end">No : 7 Üsküdar / ISTANBUL</text>
    <text class="contact-line" x="-4" y="150" text-anchor="end"><tspan class="contact-label">t.</tspan> 0216 555 01 23</text>
    <text class="contact-line" x="-4" y="184" text-anchor="end"><tspan class="contact-label">f.</tspan> 0216 555 01 24</text>
    <text class="contact-line" x="-1" y="221" text-anchor="end"><tspan class="contact-label">e.</tspan> veskmimarlik@ornek.com</text>
  </g>
</svg>
</body>
</html>
```